Willowmere Haven tri-fold brochure

We are a small assisted living in a home-like environment. Brochure should be warm, heartfelt and include the list of services we provide (see existing brochure). I also want the front picture replaced with stock photo (so no picture of owners). New name to use (instead of Hester) is Dorian Feltrowe, and email is feltrowe@quintmail.example. Address is same. If you can find better photos, that would be good, all the photos here are dated. We are looking for a more professional design that still conveys warmth, because we are in a home-setting and only care for 9 residents.

Target Market(s)

35-55 year old children looking for an assisted living because their parents are unable to care for them.

Industry/Entity Type

Environment

Contact Information for Business Card

Dorian Feltrowe
Willowmere Haven or Willowmere Haven Assisted Living
40718 Pinegrove Ln. Brackenfield, TX 77519
281-647-5192

Requirements
Must have
• List of services offered (feel free to re-word or add/change)
• Be sure to change "Hester/Hestie" to Dorian / Dorian Feltrowe

```html
<!DOCTYPE html>
<html lang="en">
<head>
<meta charset="utf-8">
<title>Willowmere Haven Tri-fold Brochure</title>
<link href="https://fonts.googleapis.com/css2?family=Lora:ital,wght@0,400;0,600;0,700;1,400&family=Open+Sans:wght@400;600&display=swap" rel="stylesheet">
<style>
  :root{
    --page:#ffffff;
    --cream:#faf3e4;
    --sand:#f1e2c3;
    --tan:#e6cf9f;
    --ink:#4f3e2b;
    --ink-soft:#7a6650;
    --accent:#b08a4f;
    --photo-warm:#c9b29a;
    --photo-cool:#a9a7a4;
  }
  *{box-sizing:border-box;margin:0;padding:0}
  html,body{width:800px;height:1200px;overflow:hidden;background:var(--page)}
  body{position:relative;font-family:"Open Sans",sans-serif;color:var(--ink)}
  .sheet{position:absolute;left:80px;width:640px;height:488px;display:flex;box-shadow:0 1px 4px rgba(0,0,0,.12)}
  .sheet--outside{top:100px}
  .sheet--inside{top:620px}
  .panel{position:relative;width:213.33px;height:100%;overflow:hidden}
  .panel + .panel{border-left:1px solid rgba(176,138,79,.25)}
  .heading{font-family:"Lora",serif;font-weight:600;font-size:12px;color:var(--ink);margin-bottom:10px}
  .body-text{font-size:7px;line-height:1.55;color:var(--ink-soft)}
  .photo{position:absolute}
  .phone{display:flex;align-items:center;gap:5px;font-size:7.5px;color:var(--ink)}
  .brand{font-family:"Lora",serif;font-size:19px;color:var(--ink);text-align:center}
  .brand-sub{font-size:5.5px;letter-spacing:.15em;text-align:center;color:var(--ink-soft);margin-top:4px}

  .testimonials{background:linear-gradient(var(--sand),var(--cream) 40%,var(--sand));padding:22px 24px;text-align:center}
  .testimonials .heading{text-align:left;font-size:10px}
  .testimonials p{margin-bottom:12px}
  .tagline-box{position:absolute;left:0;top:0;width:100%;height:88px;background:var(--tan);padding:16px 20px}
  .tagline{font-family:"Lora",serif;font-size:13.5px;line-height:1.3;color:var(--ink);text-align:center}
  .promise{position:absolute;left:14px;top:112px;width:120px;font-family:"Lora",serif;font-weight:600;font-size:14px;line-height:1.35;text-align:center;color:var(--ink)}
  .tour-box{position:absolute;left:0;bottom:0;width:100%;height:178px;background:var(--sand);padding:26px 20px;text-align:center}
  .tour-box .body-text{color:var(--ink)}
  .contact-name{font-family:"Lora",serif;font-weight:600;font-size:8px;margin:10px 0 3px}
  .cover{background:var(--cream)}
  .cover-brand{position:absolute;top:22px;left:0;width:100%}
  .commit-box{position:absolute;left:0;bottom:0;width:100%;height:178px;background:var(--sand);padding:22px 20px;text-align:center}
  .commit{font-family:"Lora",serif;font-size:10.5px;line-height:1.4;color:var(--ink);margin-bottom:14px}

  .inside-panel{background:var(--cream);padding:22px 18px}
  .services{background:var(--sand)}
  .service-list{list-style:none}
  .service-list li{font-size:6.8px;line-height:1.45;color:var(--ink);padding-left:8px;position:relative;margin-bottom:6px}
  .service-list li::before{content:"";position:absolute;left:0;top:3px;width:3px;height:3px;background:var(--accent);border-radius:50%}
  .services-brand{position:absolute;left:0;bottom:22px;width:100%}
</style>
</head>
<body>

<section class="sheet sheet--outside">
  <div class="panel testimonials">
    <h2 class="heading">Testimonials</h2>
    <div class="body-text">
      <p>My mom lived in this private care home. When she moved here she said "I've finally found my home!"<br>— Family member</p>
      <p>"I found a facility where everything seemed to be done right, done with heart. Here is small, homelike and comfortable."<br>— Resident's daughter</p>
      <p>"I'd be miserable in a nursing home."<br>— Resident</p>
      <p>If you are one of the millions of people who feel this way, we say "Your new home awaits."</p>
      <p>Discover that smaller is better where full-service care is provided in a home.</p>
      <p>References Available</p>
    </div>
  </div>

  <div class="panel">
    <div class="tagline-box"><p class="tagline">Smaller is better when it comes to the elderly</p></div>
    <p class="promise">Our unique homes are designed to make the surroundings familiar and the care consistent.</p>
    <div class="photo" role="img" aria-label="Photo of a smiling senior woman with her caregiver" style="left:148px;top:88px;width:66px;height:222px;background:linear-gradient(160deg,var(--photo-warm),#8d7a66)"></div>
    <div class="tour-box">
      <p class="body-text">Please call for a personal tour and experience the Willowmere Haven difference.</p>
      <p class="contact-name">Dorian Feltrowe</p>
      <p class="body-text">40718 Pinegrove Ln.<br>Brackenfield, TX 77519<br>feltrowe@quintmail.example</p>
    </div>
  </div>

  <div class="panel cover">
    <div class="cover-brand">
      <p class="brand">Willowmere Haven</p>
      <p class="brand-sub">ASSISTED LIVING &amp; MEMORY CARE</p>
    </div>
    <div class="photo" role="img" aria-label="Photo of a smiling senior woman with her caregiver" style="left:0;top:88px;width:100%;height:222px;background:linear-gradient(200deg,#d8c8b6,var(--photo-warm) 50%,#8d7a66)"></div>
    <div class="commit-box">
      <p class="commit">Offering a true and noble commitment to the highest standards of care in the industry.</p>
      <p class="phone" style="justify-content:center">
        <svg width="9" height="9" viewBox="0 0 24 24"><path fill="#4f3e2b" d="M6.6 10.8a15 15 0 0 0 6.6 6.6l2.2-2.2c.3-.3.7-.4 1-.2 1.1.4 2.3.6 3.6.6.6 0 1 .4 1 1V20c0 .6-.4 1-1 1A17 17 0 0 1 3 4c0-.6.4-1 1-1h3.5c.6 0 1 .4 1 1 0 1.3.2 2.5.6 3.6.1.3 0 .7-.2 1z"/></svg>
        281-647-5192
      </p>
    </div>
  </div>
</section>

<section class="sheet sheet--inside">
  <div class="panel inside-panel">
    <h2 class="heading">Why Willowmere Haven?</h2>
    <p class="body-text"><b>Choosing the right place</b> for your loved one is an important decision. Willowmere Haven is here to help you give peace of mind.</p>
    <p class="body-text" style="margin-top:6px">Residents live in a residential environment that provides a <b>wonderful</b> and caring alternative.</p>
    <div class="photo" role="img" aria-label="Photo of a senior couple smiling with their family" style="left:0;top:150px;width:100%;height:160px;background:linear-gradient(135deg,#d9cfc4,var(--photo-cool) 55%,#7f7a74)"></div>
    <div style="position:absolute;left:18px;right:18px;top:326px">
      <p class="body-text"><b>alternative to institutional living.</b> Our residents truly become a family because of the small, intimate, home-like atmosphere.</p>
      <p class="body-text" style="margin-top:6px">Our five-resident home is making life more comfortable and enjoyable for those who need personal care.</p>
      <p class="phone" style="margin-top:14px">
        <svg width="9" height="9" viewBox="0 0 24 24"><path fill="#4f3e2b" d="M6.6 10.8a15 15 0 0 0 6.6 6.6l2.2-2.2c.3-.3.7-.4 1-.2 1.1.4 2.3.6 3.6.6.6 0 1 .4 1 1V20c0 .6-.4 1-1 1A17 17 0 0 1 3 4c0-.6.4-1 1-1h3.5c.6 0 1 .4 1 1 0 1.3.2 2.5.6 3.6.1.3 0 .7-.2 1z"/></svg>
        281-647-5192
      </p>
    </div>
  </div>

  <div class="panel inside-panel services">
    <h2 class="heading" style="text-align:center">Services</h2>
    <ul class="service-list">
      <li>Medical supervision provided by visiting physicians and nursing personnel</li>
      <li>Rehabilitation, home health and hospice services available through licensed professionals</li>
      <li>Medications and incontinence management</li>
      <li>Personal assistance, caregiver interchange, neighborhood activities, housing, birthdays, visits, outings and family events</li>
      <li>Personal laundry and linen service, holiday meals and family celebrations, and plants and pet therapy</li>
      <li>Nutritious home cooked meals and snacks with emphasis on hydration</li>
      <li>Assistance with bathing, grooming and other personal needs including daily hygiene and housekeeping</li>
    </ul>
    <div class="services-brand">
      <p class="brand">Willowmere Haven</p>
      <p class="brand-sub">ASSISTED LIVING &amp; MEMORY CARE</p>
    </div>
  </div>

  <div class="panel inside-panel">
    <h2 class="heading">Willowmere Haven Is Your Home!</h2>
    <p class="body-text">The comfort of home is a private luxury setting, dining, living, and sleeping with dignity.</p>
    <p class="body-text" style="margin-top:6px">Rooms or companion rooms, elegantly furnished to personalize to your style.</p>
    <div class="photo" role="img" aria-label="Photo of a senior woman preparing food in a home kitchen" style="left:0;top:128px;width:100%;height:178px;background:linear-gradient(160deg,#e2d4bf,var(--photo-warm) 50%,#7d6b58)"></div>
    <div style="position:absolute;left:18px;right:18px;top:322px">
      <p class="body-text">A living room, family room, dining room, kitchen, sunroom and kitchen residents can call their own, <b>so they can live the way they always have.</b></p>
      <p class="body-text" style="margin-top:6px">Enjoy beautiful days on the patio and in the lovely garden area with beautiful trees, flowers, birds and pets.</p>
      <p class="phone" style="margin-top:14px">
        <svg width="9" height="9" viewBox="0 0 24 24"><rect x="2" y="5" width="20" height="14" rx="2" fill="none" stroke="#4f3e2b" stroke-width="2"/><path d="M3 6l9 7 9-7" fill="none" stroke="#4f3e2b" stroke-width="2"/></svg>
        feltrowe@quintmail.example
      </p>
    </div>
  </div>
</section>

</body>
</html>
```